Fernleigh Drafting - Flyer Design

I'm looking for good designs of the 2 sided flyer size DL (210 x 95 mm)
Please make sure the design is in the same colours as my business card. Image attached.
Include Architectural plan at the background.
Please note that some words are in capital letters...
FRONT PAGE including :
Are you planning to RENOVATE, EXTEND the house, build new GRANNY FLAT?
Do you need assistance with DA , COMPLYING DEVELOPMENT?
Is your building budget tight and you DON'T WANT to spend it on the ARCHITECTURAL FEES?
For free obligation quote contact:
FERNLEIGH DRAFTING
fernleighdrafting@mailvane.com.au
Dorota - 0491 827 604
For more details check: www.fernleighdrafting.com.au
Follow us on facebook: www.socialvine.com/fernleighdrafting
BACK PAGE including:
Services
- Building Design
- Architectural Drafting
- 3D Modelling
- Terval Assessment
- Building Specifications
- Council Submission Services
- Coordination with Building Professionals
Contact Dorota on 0491 827 604 or fernleighdrafting@mailvane.com.au for obligation free quote

```html
<!DOCTYPE html>
<html lang="en">
<head>
<meta charset="utf-8">
<title>Fernleigh Drafting – DL Flyer</title>
<link rel="stylesheet" href="https://fonts.googleapis.com/css2?family=Mulish:wght@400;600;700;800&family=Arimo:wght@400&display=swap">
<style>
  :root {
    --sky: #1ba3dc;
    --sky-text: #1c9fd9;
    --sky-soft: #86b4e2;
    --navy-line: #2a6fc4;
    --grey-band: #8b8b8d;
    --ink: #2b2b2b;
    --paper: #ffffff;
    --backdrop: #ecebe8;
    --photo-top: #c9cdd1;
    --photo-house: #d8cba8;
    --photo-lawn: #6c9a3c;
    --plan-light: #f4f5f6;
    --plan-mid: #dfe2e5;
  }
  * { box-sizing: border-box; margin: 0; padding: 0; }
  html, body { width: 1156px; height: 1200px; overflow: hidden; }
  body { background: var(--backdrop); position: relative; font-family: "Mulish", sans-serif; color: var(--ink); }

  .flyer {
    position: absolute; top: 73px; width: 478px; height: 1054px;
    background: var(--paper); overflow: hidden;
    box-shadow: 0 3px 10px rgba(0,0,0,.25);
  }
  .flyer--front { left: 68px; }
  .flyer--back { left: 611px; }

  .hero { position: absolute; top: 0; left: 0; width: 100%; height: 410px; }
  .hero--house { background: linear-gradient(180deg, var(--photo-top) 0%, var(--photo-house) 30%, var(--photo-house) 78%, var(--photo-lawn) 92%); }
  .hero--plans { background: linear-gradient(160deg, var(--plan-light) 0%, var(--plan-mid) 55%, var(--plan-light) 100%); }

  .hero-swoosh { position: absolute; top: 340px; left: 0; width: 478px; height: 80px; }

  .questions { position: absolute; top: 430px; left: 0; width: 100%; text-align: center; z-index: 2; }
  .questions p { font-size: 23px; line-height: 33px; letter-spacing: .4px; margin-bottom: 12px; }
  .questions .key { color: var(--sky-text); font-weight: 700; font-size: 25px; letter-spacing: 1px; }

  .services { position: absolute; top: 425px; left: 0; width: 100%; text-align: center; z-index: 2; }
  .services h2 { font-size: 22px; font-weight: 800; margin-bottom: 4px; }
  .services ul { list-style: none; }
  .services li { font-size: 23px; line-height: 33px; letter-spacing: .4px; }
  .services li::before { content: "• "; }

  .footer-wave { position: absolute; left: 0; top: 745px; width: 478px; height: 309px; }
  .contact { position: absolute; left: 0; top: 795px; width: 100%; text-align: center; color: var(--paper); font-family: "Arimo", sans-serif; }
  .contact .lead { font-size: 17px; }
  .brand { font-family: "Mulish", sans-serif; font-weight: 800; font-size: 38px; line-height: 42px; margin: 8px 0 22px; letter-spacing: .5px; }
  .contact .line { font-size: 22px; line-height: 29.5px; }
</style>
</head>
<body>

<article class="flyer flyer--front">
  <div class="hero hero--house" role="img" aria-label="Photo of a two-storey weatherboard family house with front lawn"></div>
  <svg class="hero-swoosh" viewBox="0 0 478 80" aria-hidden="true">
    <path d="M0,30 Q210,105 478,22 L478,80 L0,80 Z" fill="var(--navy-line)"/>
    <path d="M0,42 Q220,112 478,38 L478,80 L0,80 Z" fill="var(--grey-band)"/>
    <path d="M0,50 Q230,122 478,52 L478,80 L0,80 Z" fill="var(--paper)"/>
  </svg>

  <section class="questions">
    <p>Are you planning to <span class="key">RENOVATE,</span><br><span class="key">EXTEND</span> the house, build new<br><span class="key">GRANNY FLAT?</span></p>
    <p>Do you need assistance with <span class="key">DA ,</span><br><span class="key">COMPLYING DEVELOPMENT?</span></p>
    <p>Is your building budget tight and you<br><span class="key">DON'T WANT</span> to spend it on the<br><span class="key">ARCHITECTURAL FEES?</span></p>
  </section>

  <svg class="footer-wave" viewBox="0 0 478 309" aria-hidden="true">
    <path d="M0,12 Q230,-10 478,48 L478,309 L0,309 Z" fill="var(--grey-band)"/>
    <path d="M0,28 Q240,8 478,62 L478,309 L0,309 Z" fill="var(--sky-soft)"/>
    <path d="M0,42 Q250,24 478,74 L478,309 L0,309 Z" fill="var(--sky)"/>
  </svg>
  <section class="contact">
    <p class="lead">For free obligation quote contact:</p>
    <p class="brand">Fernleigh<br>Drafting</p>
    <p class="line">fernleighdrafting@mailvane.com.au</p>
    <p class="line">Dorota - 0491 827 604</p>
    <p class="line">www.fernleighdrafting.com.au</p>
    <p class="line">Socialvine : fernleighdrafting</p>
  </section>
</article>

<article class="flyer flyer--back">
  <div class="hero hero--plans" role="img" aria-label="Rolled architectural floor plans lying on a printed blueprint"></div>
  <svg class="hero-swoosh" viewBox="0 0 478 80" aria-hidden="true">
    <path d="M0,30 Q210,105 478,22 L478,80 L0,80 Z" fill="var(--navy-line)"/>
    <path d="M0,42 Q220,112 478,38 L478,80 L0,80 Z" fill="var(--grey-band)"/>
    <path d="M0,50 Q230,122 478,52 L478,80 L0,80 Z" fill="var(--paper)"/>
  </svg>

  <section class="services">
    <h2>Services</h2>
    <ul>
      <li>Building Design</li>
      <li>Architectural Drafting</li>
      <li>3D Modelling</li>
      <li>Terval Assessment</li>
      <li>Building Specifications</li>
      <li>Council Submission Services</li>
      <li>Coordination with Building<br>Professionals</li>
    </ul>
  </section>

  <svg class="footer-wave" viewBox="0 0 478 309" aria-hidden="true">
    <path d="M0,12 Q230,-10 478,48 L478,309 L0,309 Z" fill="var(--grey-band)"/>
    <path d="M0,28 Q240,8 478,62 L478,309 L0,309 Z" fill="var(--sky-soft)"/>
    <path d="M0,42 Q250,24 478,74 L478,309 L0,309 Z" fill="var(--sky)"/>
  </svg>
  <section class="contact">
    <p class="lead">For free obligation quote contact:</p>
    <p class="brand">Fernleigh<br>Drafting</p>
    <p class="line">fernleighdrafting@mailvane.com.au</p>
    <p class="line">Dorota - 0491 827 604</p>
    <p class="line">www.fernleighdrafting.com.au</p>
    <p class="line">Socialvine : fernleighdrafting</p>
  </section>
</article>

</body>
</html>
```